Applied environmental services company startup chasing a look

Small team of practical, technical and management-focused people in a business that can write the report, do the work written up in the report cost effectively. Vertical integration from design through to application. This business will be chasing opportunities where project management melds with technical application for clients needing forestry, environmental or natural resource management work done. We need a graphic and style for use in Microsoft Word and Powerpoint. A template including fonts, headings and styles would be great. Don't have a name yet, however I do like Tallbrook Equity, Tallbrook Merit, Tallbrook Holdings...

Industry/Entity Type

It Company

Requirements
Nice to have
• I would like different shades of blue to be a part of the design.

```html
<!DOCTYPE html>
<html lang="en">
<head>
<meta charset="UTF-8">
<title>Tallbrook Equity — Slide Template</title>
<link href="https://fonts.googleapis.com/css2?family=Raleway:wght@800&family=Noto+Sans:wght@400;700&display=swap" rel="stylesheet">
<style>
  :root {
    --brand-blue: #338bab;
    --text-dark: #111111;
    --paper: #ffffff;
  }
  html, body {
    margin: 0;
    padding: 0;
    overflow: hidden;
    background: var(--paper);
  }
  .slide {
    position: relative;
    width: 1200px;
    height: 900px;
    overflow: hidden;
    background: var(--paper);
  }
  .slide-title {
    position: absolute;
    left: 97px;
    top: 112px;
    margin: 0;
    font-family: 'Raleway', sans-serif;
    font-weight: 800;
    font-size: 60px;
    line-height: 1;
    color: var(--brand-blue);
  }
  .slide-body {
    position: absolute;
    left: 97px;
    top: 254px;
    width: 1000px;
    font-family: 'Noto Sans', sans-serif;
    font-size: 32.5px;
    line-height: 49px;
    color: var(--text-dark);
  }
  .slide-body p {
    margin: 0 0 49px 0;
  }
  .corner-wave {
    position: absolute;
    left: 0;
    top: 0;
    width: 1200px;
    height: 900px;
  }
  .brand-name {
    position: absolute;
    left: 994px;
    top: 766px;
    margin: 0;
    font-family: 'Noto Sans', sans-serif;
    font-weight: 700;
    font-size: 36px;
    line-height: 42px;
    color: var(--paper);
  }
  .page-nav {
    position: absolute;
    left: 142px;
    top: 812px;
    display: flex;
    align-items: center;
    gap: 12px;
  }
  .page-number {
    width: 56px;
    height: 56px;
    border-radius: 50%;
    background: var(--brand-blue);
    color: var(--paper);
    font-family: 'Noto Sans', sans-serif;
    font-weight: 700;
    font-size: 24px;
    display: flex;
    align-items: center;
    justify-content: center;
  }
</style>
</head>
<body>
  <main class="slide">
    <h1 class="slide-title">Title Put Here</h1>

    <div class="slide-body">
      <p>Lorem ipsum dolor sit amet, consectetur adipiscing elit.<br>
      Maecenas erat diam, vehicula eget pharetra at, suscipit id<br>
      leo. Nulla felis dui, pulvinar sed metus quis, mattis lobortis<br>
      dui. Nullam metus ipsum, dictum a magna non, mattis<br>
      sagittis lacus. Morbi id dictum nibh. Suspendisse potenti.</p>
      <p>Praesent nec convallis tortor. Duis fermentum auctor<br>
      tortor. Integer ac sodales mauris.</p>
    </div>

    <svg class="corner-wave" viewBox="0 0 1200 900" aria-hidden="true">
      <path fill="var(--brand-blue)"
        d="M727,900 C800,830 820,700 925,686 C1005,676 1040,715 1100,702 C1160,688 1188,620 1200,572 L1200,900 Z"/>
    </svg>

    <p class="brand-name">Tallbrook<br>Equity</p>

    <nav class="page-nav" aria-label="Page navigation">
      <svg width="20" height="26" viewBox="0 0 20 26" aria-hidden="true">
        <polygon points="20,0 20,26 0,13" fill="var(--brand-blue)"/>
      </svg>
      <div class="page-number">2</div>
      <svg width="20" height="26" viewBox="0 0 20 26" aria-hidden="true">
        <polygon points="0,0 0,26 20,13" fill="var(--brand-blue)"/>
      </svg>
    </nav>
  </main>
</body>
</html>
```